Business Card for Coastal Bedrock Consulting

We need a business card for Coastal Bedrock Consulting. The company website address is provided below. The company logo is attached. We provide specialized permafrost services to the mining, transportation, and oil & gas industries. The card should be prepared for:
Randall Whitacre, PhD.
Coastal Bedrock Consulting
PO Box 418539
Moose Hollow, Alaska 99642
Direct: +1-907-555-0143
Email: rwhitacre@bedrockadvisory.example
Website: www.coastalbedrockconsulting.example

```html
<!DOCTYPE html>
<html lang="en">
<head>
<meta charset="utf-8">
<title>Coastal Bedrock Consulting – Business Card</title>
<link href="https://fonts.googleapis.com/css2?family=Lato:wght@400;700;900&display=swap" rel="stylesheet">
<style>
  :root {
    --stage: #3a3a3a;
    --navy: #111820;
    --paper: #ffffff;
    --silver: #b9bdc2;
    --silver-dim: #7d838a;
    --ink: #111820;
  }
  * { box-sizing: border-box; margin: 0; padding: 0; }
  html, body {
    width: 1200px; height: 875px; overflow: hidden;
    background: var(--stage);
    font-family: "Lato", Arial, sans-serif;
  }
  .canvas {
    width: 1200px; height: 875px;
    display: flex; flex-direction: column;
    align-items: center; justify-content: center; gap: 36px;
  }
  .card {
    position: relative;
    width: 660px; height: 377px;
    border-radius: 26px;
    overflow: hidden;
  }
  /* Front */
  .card-front {
    background: var(--navy);
    display: flex; align-items: center; justify-content: center;
  }
  .brand {
    display: flex; align-items: center; gap: 14px;
  }
  .brand-mark {
    width: 16px; height: 16px; background: currentColor; flex: none;
  }
  .brand-name {
    font-weight: 700; text-transform: uppercase; letter-spacing: 0.12em;
  }
  .card-front .brand { color: var(--silver); }
  .card-front .brand-name { font-size: 28px; }

  /* Back */
  .card-back { background: var(--paper); }
  .side-bar {
    position: absolute; left: 36px; top: 205px;
    width: 9px; height: 150px; background: var(--navy);
  }
  .card-back .brand {
    position: absolute; left: 62px; top: 238px; color: var(--ink);
  }
  .card-back .brand-name { font-size: 17px; letter-spacing: 0.1em; }
  .info-panel {
    position: absolute; right: 0; top: 62px;
    width: 350px; height: 180px;
    background: var(--navy); color: var(--paper);
    padding: 20px 18px 0 28px;
  }
  .person-name {
    font-weight: 900; font-size: 17px; text-transform: uppercase; letter-spacing: 0.01em;
  }
  .person-company { font-size: 13px; margin-top: 2px; margin-bottom: 10px; }
  .contact-list { list-style: none; font-size: 12.5px; line-height: 1.35; }
  .contact-list li { display: flex; align-items: flex-start; gap: 9px; margin-bottom: 4px; }
  .contact-list svg { width: 11px; height: 11px; flex: none; margin-top: 3px; fill: var(--paper); }
</style>
</head>
<body>
<main class="canvas">
  <section class="card card-front" aria-label="Card front">
    <div class="brand">
      <span class="brand-mark"></span>
      <span class="brand-name">Coastal Bedrock Consulting</span>
    </div>
  </section>

  <section class="card card-back" aria-label="Card back">
    <div class="side-bar"></div>
    <div class="brand">
      <span class="brand-mark"></span>
      <span class="brand-name">Coastal Bedrock Consulting</span>
    </div>
    <div class="info-panel">
      <h1 class="person-name">Randall Whitacre, PhD.</h1>
      <p class="person-company">Coastal Bedrock Consulting</p>
      <ul class="contact-list">
        <li>
          <svg viewBox="0 0 12 12"><path d="M6 0a4 4 0 0 0-4 4c0 3 4 8 4 8s4-5 4-8a4 4 0 0 0-4-4zm0 5.6A1.6 1.6 0 1 1 6 2.4a1.6 1.6 0 0 1 0 3.2z"/></svg>
          <span>PO Box 418539<br>Moose Hollow, Alaska 99642</span>
        </li>
        <li>
          <svg viewBox="0 0 12 12"><path d="M2.4 0.6l1.8 2.4-1 1.2c.7 1.6 1.9 2.8 3.6 3.6l1.2-1 2.4 1.8-1 2.4C4.8 10.8 1.2 7.2.2 1.6z"/></svg>
          <span>+1-907-555-0143</span>
        </li>
        <li>
          <svg viewBox="0 0 12 12"><path d="M0 2h12v8H0zM1 3l5 3.6L11 3v-.2H1z" fill-rule="evenodd"/></svg>
          <span>rwhitacre@bedrockadvisory.example</span>
        </li>
        <li>
          <svg viewBox="0 0 12 12"><circle cx="6" cy="6" r="6"/><path d="M0 6h12M6 0c2 2 2 10 0 12M6 0c-2 2-2 10 0 12" stroke="#111820" stroke-width="1" fill="none"/></svg>
          <span>coastalbedrockconsulting.example</span>
        </li>
      </ul>
    </div>
  </section>
</main>
</body>
</html>
```